Business card design needed

Design:
Want the logo/design to have an enviromental feel
Simple look not to busy

Company Info:
Pre purchase building and pest inspections
Registered building practitoner DB-U 58147 (please include building commission logo in design)

Industry/Entity Type

Building

Contact Information for Business Card

Company name:
Fernvale Building and Pest inspections

Inspectors:
Dean Harker 0451 278 914
Greg Sutcliffe 0419 562 843
Email: fernvalebpi@mailpost.example

```html
<!DOCTYPE html>
<html lang="en">
<head>
<meta charset="utf-8">
<title>Fernvale Building and Pest inspections – Business Card</title>
<link rel="stylesheet" href="https://fonts.googleapis.com/css2?family=Roboto:wght@500;700&display=swap">
<style>
  :root {
    --backdrop: #e9e6e1;
    --green-light: #8fd45a;
    --green: #4cb53a;
    --green-dark: #1f8a2f;
    --blue: #1f8fe0;
    --blue-dark: #1758b8;
    --white: #ffffff;
    --paper: #f2f2f2;
    --shadow: rgba(0, 0, 0, 0.22);
  }
  * { box-sizing: border-box; margin: 0; padding: 0; }
  html, body { width: 1200px; height: 900px; overflow: hidden; }
  body {
    background: var(--backdrop);
    font-family: "Roboto", Arial, sans-serif;
    display: flex;
    flex-direction: column;
    align-items: center;
    justify-content: center;
    gap: 40px;
  }
  .card {
    position: relative;
    width: 700px;
    height: 400px;
    overflow: hidden;
    box-shadow: 0 10px 26px var(--shadow);
  }
  .card-art { position: absolute; inset: 0; width: 100%; height: 100%; }
  .wordmark {
    position: absolute;
    color: var(--green-dark);
    font-weight: 700;
    line-height: 1.05;
  }
  .wordmark-name { display: block; }
  .wordmark-tagline { display: block; }
  .card-front .wordmark {
    left: 0; right: 0; top: 150px;
    text-align: center;
  }
  .card-front .wordmark-name { font-size: 58px; letter-spacing: -1px; }
  .card-front .wordmark-tagline { font-size: 30px; margin-top: 4px; }
  .card-back .wordmark {
    right: 40px; top: 50px;
    text-align: right;
  }
  .card-back .wordmark-name { font-size: 40px; letter-spacing: -0.5px; }
  .card-back .wordmark-tagline { font-size: 21px; margin-top: 2px; }
  .contact {
    position: absolute;
    left: 48px; top: 206px;
    color: var(--white);
    font-weight: 700;
    list-style: none;
  }
  .contact-label { font-size: 19px; font-weight: 500; margin-bottom: 6px; }
  .contact-line { font-size: 24px; line-height: 36px; }
</style>
</head>
<body>

  <section class="card card-front" aria-label="Business card front">
    <svg class="card-art" viewBox="0 0 700 400" preserveAspectRatio="none" aria-hidden="true">
      <defs>
        <linearGradient id="frontGreen" x1="0" y1="0" x2="1" y2="1">
          <stop offset="0" stop-color="var(--green-light)"/>
          <stop offset="1" stop-color="var(--green-dark)"/>
        </linearGradient>
        <linearGradient id="frontBlue" x1="0" y1="0" x2="1" y2="1">
          <stop offset="0" stop-color="var(--blue)"/>
          <stop offset="1" stop-color="var(--blue-dark)"/>
        </linearGradient>
      </defs>
      <rect width="700" height="400" fill="url(#frontGreen)"/>
      <path d="M700 40 L700 400 L40 400 C300 390 560 330 700 40 Z" fill="url(#frontBlue)"/>
      <path d="M330 0 L700 0 L700 60 C610 300 380 370 0 380 L0 330 C220 300 340 180 330 0 Z" fill="var(--paper)"/>
    </svg>
    <h1 class="wordmark">
      <span class="wordmark-name">Fernvale Building</span>
      <span class="wordmark-tagline">and Pest inspections</span>
    </h1>
  </section>

  <section class="card card-back" aria-label="Business card back">
    <svg class="card-art" viewBox="0 0 700 400" preserveAspectRatio="none" aria-hidden="true">
      <defs>
        <linearGradient id="backGreen" x1="0" y1="0" x2="0" y2="1">
          <stop offset="0" stop-color="var(--green-light)"/>
          <stop offset="1" stop-color="var(--green)"/>
        </linearGradient>
      </defs>
      <rect width="700" height="400" fill="var(--paper)"/>
      <path d="M0 0 L34 0 C150 170 400 252 700 252 L700 400 L0 400 Z" fill="url(#backGreen)"/>
      <path d="M22 0 C140 160 400 236 700 236" fill="none" stroke="var(--blue)" stroke-width="6"/>
    </svg>
    <h2 class="wordmark">
      <span class="wordmark-name">Fernvale Building</span>
      <span class="wordmark-tagline">and Pest inspections</span>
    </h2>
    <ul class="contact">
      <li class="contact-label">Inspectors:</li>
      <li class="contact-line">Dean Harker 0451 278 914</li>
      <li class="contact-line">Greg Sutcliffe 0419 562 843</li>
      <li class="contact-line">Email: fernvalebpi@mailpost.example</li>
      <li class="contact-line">Registered building practitoner DB-U 58147</li>
    </ul>
  </section>

</body>
</html>
```